Lumora Glow Teeth Whitening Pen Box

We would like to have some new packaging designed for our Teeth Whitening pens.
We are preparing top re-launch this product and aim to get this into supermarkets, pharmacies and other beauty clinics/dentists etc..
We would like the box to be 145mm high 65mm wide and 25mm deep.
I have attached our new logo, all writing that is required on the back of the box, a sample of our current design which was never completed and an image of a similar product packaging from overseas which we absolutely love.
We would like our box to be similar to what we have already started designing but obviously much better and similar to the other product packaging image attached.
On the front of the box, rather than having it say " your best smile in just one hour" can you please send across an image with each of these so we can see what looks best. You can remove the other writing on the front of the box or put it elsewhere depending on what looks best.
"Clinically Proven Whitening Technology"
"Whitening Technology Used By Dentists"
On the sides of the packaging we would like it to say "Revolutionary Whitening Power"
The flavour of the gel is " Fresh Mint"
Could say:
Ideal to remove staining from coffee, wine, smoking etc..
Writing that should be on the back of the box:
DIRECTIONS
1.Rinse mouth with water and wipe teeth dry.
2.Rotate base of pen to dispense the gel
3.Hold a wide smile and apply gel carefully to teeth while avoiding gums
4.Let gel dry on teeth for 10 minutes then rinse mouth with water
5.Refrain from eating, drinking or smoking for 30 minutes following treatment.
6. Apply twice per day for up to five days. To maintain results reapply once or twice a week as required.
CAUTION
•Do not use if you are under 16 years old, are pregnant, breastfeeding or have any pre-existing dental or gum problems.
•In rare cases, tooth sensitivity may occur. If sustained sensitivity occurs, stop using product.
•Do not use for more than 14 consecutive days unless advised by a dentist.
INGREDIENTS
Percarbamide, Glycerol, Propylene Glycol, Flavouring
Storage: Avoid sunlight & keep in cool.
Expires: 30 December 2014
www.lumoraglow.co.nz
enquiries@lumoraglow.co.nz
Freephone: 0800 517 293
Age: 20-45
Gender: Mostly female but should appeal to both
Supermarket/pharmacy shoppers
Product
Must have
- Must have all directions and caution labels outlined in the description.

```html
<!DOCTYPE html>
<html lang="en">
<head>
<meta charset="utf-8">
<title>Lumora Glow Teeth Whitening Pen – Packaging</title>
<link href="https://fonts.googleapis.com/css2?family=Source+Sans+3:ital,wght@0,300;0,400;0,600;0,700;1,600;1,700&display=swap" rel="stylesheet">
<style>
  :root{
    --sky:#4db3e6;
    --navy:#27306f;
    --ink:#3d4585;
    --wave-1:#e9f5fb;
    --wave-2:#9fd1ea;
    --wave-3:#3c9cc9;
    --rule:#222;
    --paper:#ffffff;
    --silver-1:#f4f4f4;
    --silver-2:#9a9ea3;
  }
  *{box-sizing:border-box;margin:0;padding:0}
  html,body{width:1200px;height:900px;overflow:hidden;background:var(--paper)}
  body{position:relative;font-family:"Source Sans 3",sans-serif;color:var(--navy)}

  .panel{position:absolute;overflow:hidden;border:1px solid var(--rule);background:var(--paper)}
  .panel--front-detail{left:82px;top:18px;width:472px;height:431px}
  .panel--back-detail{left:82px;top:457px;width:472px;height:430px}
  .panel--front{left:748px;top:120px;width:300px;height:680px;border-color:#777}

  .fold{position:absolute;top:0;bottom:0;border-left:1px solid var(--rule)}

  .side-claim{position:absolute;white-space:nowrap;font-weight:300;color:var(--ink);
    writing-mode:vertical-rl;transform:rotate(180deg)}

  .waves{position:absolute;left:0;right:0;bottom:0}

  .brand{font-weight:400;color:var(--sky);letter-spacing:-.5px;display:flex;align-items:center;gap:8px}
  .brand__dot{width:10px;height:10px;border-radius:50%;background:var(--sky)}
  .product-name{font-weight:400;color:var(--navy)}

  .pen{position:absolute;border-radius:6px 6px 2px 2px;
    background:linear-gradient(90deg,var(--silver-2),var(--silver-1) 35%,#fff 50%,var(--silver-2) 80%,#cfd2d5)}

  /* back copy */
  .copy{position:absolute;left:146px;top:30px;width:315px;font-size:10.5px;line-height:14px;color:var(--ink)}
  .copy h3{font-size:10.5px;font-weight:700;color:var(--navy);margin-bottom:12px}
  .copy ol{list-style:none}
  .copy ol li{margin-bottom:12px;padding-left:12px;text-indent:-12px}
  .copy ol b{font-weight:700}
  .copy ul{list-style:none;margin-top:0}
  .copy ul li{margin-bottom:12px;padding-left:10px;position:relative}
  .copy ul li::before{content:"•";position:absolute;left:0}
  .caution{margin-top:52px}

  /* front panel */
  .ribbon{position:absolute;left:0;right:0;top:455px;height:130px;background:rgba(255,255,255,.82);
    transform:skewY(-6deg)}
  .claims{position:absolute;left:14px;top:472px;width:180px;transform:rotate(-8deg);
    font-style:italic;font-weight:700;color:var(--navy);font-size:13px;line-height:14px}
  .claims p+p{margin-top:12px}
  .flavour{position:absolute;left:0;right:0;top:603px;height:22px;background:var(--wave-3);
    color:#fff;font-weight:700;font-style:italic;font-size:13px;text-align:center;line-height:22px;
    transform:skewY(-3deg)}
  .volume{position:absolute;left:0;right:0;top:648px;text-align:center;font-size:9px;color:var(--ink);transform:rotate(-3deg)}
</style>
</head>
<body>

<!-- Front panel with side strip, detail -->
<section class="panel panel--front-detail" aria-label="Front panel and side">
  <svg class="waves" width="472" height="130" viewBox="0 0 472 130" aria-hidden="true">
    <defs>
      <linearGradient id="wA" x1="0" y1="0" x2="1" y2="1">
        <stop offset="0" stop-color="#ffffff"/><stop offset=".6" stop-color="#bfe2f3"/><stop offset="1" stop-color="#6db9df"/>
      </linearGradient>
    </defs>
    <path d="M0 45 L472 20 L472 130 L0 130Z" fill="url(#wA)"/>
    <path d="M0 40 C150 38 300 30 472 18" stroke="#3c9cc9" stroke-width="1.5" fill="none"/>
    <path d="M0 110 C120 80 260 40 472 10" stroke="#5aaedb" stroke-width="1" fill="none" opacity=".7"/>
  </svg>
  <div class="fold" style="left:95px"></div>
  <div class="fold" style="left:443px"></div>
  <div class="side-claim" style="left:14px;bottom:-18px;font-size:34px">Revolutionary Whitening Power</div>

  <div class="brand" style="position:absolute;left:135px;top:38px;font-size:42px">Lumora Glow<span class="brand__dot"></span></div>
  <div class="product-name" style="position:absolute;left:137px;top:140px;font-size:30px">TeethWhitening Pen</div>

  <svg style="position:absolute;left:218px;top:212px" width="100" height="100" viewBox="0 0 100 100" aria-label="Whitening technology used by dentists">
    <defs>
      <path id="arcTop1" d="M14 50 A36 36 0 0 1 86 50"/>
      <path id="arcBot1" d="M12 50 A38 38 0 0 0 88 50"/>
    </defs>
    <circle cx="50" cy="50" r="41" fill="none" stroke="var(--navy)" stroke-width="16"/>
    <text font-size="8.5" font-weight="600" fill="#fff" font-family="Source Sans 3,sans-serif"><textPath href="#arcTop1" startOffset="50%" text-anchor="middle">WHITENING TECHNOLOGY</textPath></text>
    <text font-size="8.5" font-weight="600" fill="#fff" font-family="Source Sans 3,sans-serif" dy="6"><textPath href="#arcBot1" startOffset="50%" text-anchor="middle">USED BY DENTISTS</textPath></text>
  </svg>

  <div class="pen" role="img" aria-label="Photo of the whitening pen" style="left:378px;top:200px;width:48px;height:240px"></div>
</section>

<!-- Back panel with side strip, detail -->
<section class="panel panel--back-detail" aria-label="Back panel and side">
  <svg style="position:absolute;left:0;top:0" width="472" height="430" viewBox="0 0 472 430" aria-hidden="true">
    <defs>
      <linearGradient id="wB" x1="0" y1="0" x2="1" y2="1">
        <stop offset="0" stop-color="#ffffff"/><stop offset=".5" stop-color="#d7edf7"/><stop offset="1" stop-color="#5fb3dc"/>
      </linearGradient>
    </defs>
    <rect x="134" y="0" width="338" height="430" fill="#f4f9fc"/>
    <path d="M0 280 C150 250 300 200 472 150 L472 430 L0 430Z" fill="url(#wB)" opacity=".8"/>
    <path d="M130 300 L472 90 L472 140 L200 300Z" fill="#9a8fcf" opacity=".25"/>
    <path d="M0 240 C150 235 320 215 472 200" stroke="#3c9cc9" stroke-width="1.2" fill="none"/>
  </svg>
  <div class="fold" style="left:124px"></div>
  <div class="side-claim" style="left:28px;bottom:-30px;font-size:34px">Revolutionary Whitening Power</div>

  <div class="copy">
    <h3>DIRECTIONS</h3>
    <ol>
      <li><b>1)</b> Rinse mouth with water and wipe teeth dry. Rotate base of pen to dispense the gel.</li>
      <li><b>2)</b> Hold a wide smile and apply gel carefully to teeth while avoiding gums.</li>
      <li><b>3)</b> Let gel dry on teeth for 10 minutes then rinse mouth with water.</li>
      <li><b>4)</b> Refrain from eating, drinking or smoking for 30 minutes following treatment.</li>
      <li><b>5)</b> Apply twice per day for up to five days. To maintain results reapply once or twice a week as required.</li>
    </ol>
    <h3 class="caution">CAUTION</h3>
    <ul>
      <li>Do not use if you are under 16 years old, are pregnant, breastfeeding or have any pre-existing dental or gum problems.</li>
      <li>In rare cases, tooth sensitivity may occur. If sustained sensitivity occurs, stop using product.</li>
      <li>Do not use for more than 14 consecutive days unless advised by a dentist.</li>
    </ul>
  </div>
</section>

<!-- Front panel, full -->
<section class="panel panel--front" aria-label="Box front">
  <svg style="position:absolute;left:0;top:0" width="300" height="680" viewBox="0 0 300 680" aria-hidden="true">
    <defs>
      <linearGradient id="wC" x1="0" y1="0" x2="0" y2="1">
        <stop offset="0" stop-color="#ffffff"/><stop offset=".4" stop-color="#cfe9f6"/><stop offset="1" stop-color="#4aa6d4"/>
      </linearGradient>
    </defs>
    <path d="M0 330 L300 255 L300 680 L0 680Z" fill="url(#wC)"/>
    <path d="M0 330 L300 255" stroke="#2f8fc2" stroke-width="3"/>
    <path d="M0 420 C90 380 200 330 300 320" stroke="#5aaedb" stroke-width="1" fill="none"/>
    <path d="M0 600 L300 585 L300 680 L0 680Z" fill="#7cc2e3" opacity=".6"/>
  </svg>

  <div class="brand" style="position:absolute;left:30px;top:60px;font-size:34px">Lumora Glow<span class="brand__dot"></span></div>
  <div class="product-name" style="position:absolute;left:32px;top:150px;font-size:25px;transform:rotate(-4deg)">TeethWhitening Pen</div>

  <svg style="position:absolute;left:100px;top:225px" width="90" height="90" viewBox="0 0 100 100" aria-label="Whitening technology used by dentists">
    <defs>
      <path id="arcTop2" d="M14 50 A36 36 0 0 1 86 50"/>
      <path id="arcBot2" d="M12 50 A38 38 0 0 0 88 50"/>
    </defs>
    <circle cx="50" cy="50" r="41" fill="none" stroke="var(--navy)" stroke-width="16"/>
    <text font-size="8.5" font-weight="600" fill="#fff" font-family="Source Sans 3,sans-serif"><textPath href="#arcTop2" startOffset="50%" text-anchor="middle">WHITENING TECHNOLOGY</textPath></text>
    <text font-size="8.5" font-weight="600" fill="#fff" font-family="Source Sans 3,sans-serif" dy="6"><textPath href="#arcBot2" startOffset="50%" text-anchor="middle">USED BY DENTISTS</textPath></text>
  </svg>

  <div class="ribbon"></div>
  <div class="pen" role="img" aria-label="Photo of the whitening pen with its cap" style="left:232px;top:200px;width:40px;height:400px"></div>
  <div class="pen" role="img" aria-label="Photo of the pen cap" style="left:190px;top:500px;width:36px;height:110px"></div>

  <div class="claims">
    <p>Clinically Proven<br>Whitening Technology</p>
    <p>Ideal for remove staining<br>from coffee, wine &amp; smoking</p>
  </div>

  <div class="flavour">FRESH MINT</div>
  <div class="volume">0.04floz ℮2ml</div>
</section>

</body>
</html>
```